Flyer to promote new Commercial HVAC Preventative Maintenance clients

This flyer will be in the body of emails that will be sent to new, existing, and/or potential commericial buildings HVAC clients. It will have the least amount of words used, but it will convey the point with pertinent pictorial and graphics. It will show the value of a Periodic/Preventative routine maintenance to lower operating costs of their commericial buildings (i.e. office, medical, shopping centers, apartment, warehouse facility, etc.), in the following ways:
1) Reduce monthly power usage,
2) Reduce emergency HVAC service calls,
3) Reduce costly repairs costs,
4) Reduce HVAC down-times and angry tenants,
5) Increases the life expectancy of the existing and/or new HVAC equipment in the building and/or the equipment's' early replacement costs,
6) Reduces tenant's early termination of their lease and law suits against the landlords,
7) Increases tenant's renewal of the lease and agree to pay the increase rental rates,
8) Reduces unhappy customers and increases tenant's productivity,
9) By reducing the landlord's expenses, the value of the property will increase considerably and profitable to sell their holdings, or refinance and keep their holdings with an increased ROI (Return On Investment).

Landlords can not depend on their tenants' obligation to maintain the landlords' major assets, which is their HVAC equipment and systems.

With the periodic maintenance done by one reliable and licensed HVAC company, the will not use different companies that may or may not do the right repair job on their unit and hurt their bottom line and increase HVAC replacement COSTLY rates.

```html
<!DOCTYPE html>
<html lang="en">
<head>
<meta charset="utf-8">
<title>Vero Climate – Commercial HVAC Maintenance</title>
<link href="https://fonts.googleapis.com/css2?family=Montserrat:wght@400;500;700&family=Open+Sans:wght@400&family=Bebas+Neue&display=swap" rel="stylesheet">
<style>
  :root{
    --stage:#5a5a5a;
    --paper:#ffffff;
    --ink:#2b2b2b;
    --muted:#4a4a4a;
    --brand-blue:#1f7fc4;
    --brand-orange:#e8552a;
    --tile:#cfe6f1;
    --band-dark:#0f3f7c;
    --band-mid:#1c5fae;
  }
  *{box-sizing:border-box;margin:0;padding:0}
  html,body{width:799px;height:1200px;overflow:hidden;background:var(--stage)}
  .flyer{position:absolute;left:111px;top:46px;width:578px;height:1108px;background:var(--paper);font-family:"Montserrat",sans-serif;color:var(--ink)}

  .header{position:absolute;left:0;top:0;width:100%;height:95px}
  .contact{position:absolute;top:39px;font-size:11px;line-height:14px;color:var(--muted)}
  .contact strong{display:block;font-weight:700;font-size:12px;color:var(--brand-blue)}
  .contact--web{left:22px}
  .contact--phone{right:23px;text-align:right}
  .brand{position:absolute;left:0;right:0;top:34px;display:flex;justify-content:center;align-items:center;gap:7px}
  .brand-dot{width:12px;height:12px;border-radius:50%;background:var(--brand-orange)}
  .brand-name{font-size:24px;font-weight:500;color:#5b5b5b;letter-spacing:-.3px}

  .photo{position:absolute}
  .photo--hero{left:0;top:95px;width:578px;height:299px;background:linear-gradient(180deg,#9cc3e4 0%,#b9cde0 35%,#8ea6bd 70%,#a9adb1 100%)}
  .photo--crew{left:0;top:828px;width:285px;height:155px;background:linear-gradient(180deg,#8b8b8b 0%,#3a3632 60%,#4a4744 100%)}
  .photo--roof{left:293px;top:828px;width:285px;height:155px;background:linear-gradient(180deg,#3f7fd0 0%,#c9cfd6 55%,#9aa2aa 100%)}

  .headline{position:absolute;left:0;right:0;top:408px;text-align:center;font-weight:700;font-size:17px;color:var(--brand-blue)}
  .subline{position:absolute;left:0;right:0;top:438px;text-align:center;font-size:17px;line-height:21px;font-weight:400;color:var(--ink)}

  .cta{position:absolute;left:224px;top:498px;width:131px;height:26px;background:var(--brand-orange);color:#fff;font-family:"Bebas Neue",sans-serif;font-size:21px;line-height:27px;text-align:center;border-radius:2px;box-shadow:0 1px 4px rgba(0,0,0,.25);letter-spacing:.3px}

  .benefits{position:absolute;left:20px;top:544px;display:grid;grid-template-columns:repeat(3,170px);grid-auto-rows:78px;column-gap:12px;row-gap:14px}
  .benefit{position:relative}
  .benefit::after{content:"";position:absolute;left:4px;top:4px;right:-4px;bottom:-4px;border-right:1.5px solid var(--edge);border-bottom:1.5px solid var(--edge)}
  .benefit--orange{--edge:var(--brand-orange)}
  .benefit--blue{--edge:var(--brand-blue)}
  .benefit-face{position:absolute;inset:0;z-index:1;background:var(--tile);clip-path:polygon(11px 0,100% 0,100% 100%,0 100%,0 11px);display:flex;align-items:center;justify-content:center;text-align:center;padding:0 8px;font-family:"Open Sans",sans-serif;font-size:11px;line-height:14.3px;color:var(--ink)}

  .footer{position:absolute;left:0;top:1002px;width:578px;height:106px;background:linear-gradient(160deg,var(--band-mid) 0%,var(--band-dark) 55%,var(--band-mid) 100%);color:#fff}
  .partners{position:absolute;left:38px;top:10px;font-size:16px;font-weight:400}
  .partners b{font-weight:700}
  .divider{position:absolute;left:260px;top:10px;width:3px;height:86px;background:var(--brand-orange)}
  .promise{position:absolute;left:295px;top:12px;font-size:14.5px;line-height:20.3px;font-weight:500}
</style>
</head>
<body>
<main class="flyer">
  <header class="header">
    <div class="contact contact--web">Visit Website<strong>www.veroclimate.com</strong></div>
    <div class="brand"><span class="brand-dot"></span><span class="brand-name">Vero Climate</span></div>
    <div class="contact contact--phone">Call Us Today<strong>555-014-2288</strong></div>
  </header>

  <div class="photo photo--hero" role="img" aria-label="Rooftop commercial condenser units with ductwork under a blue sky"></div>

  <h1 class="headline">Unlock Savings, Ensure Sustainability</h1>
  <p class="subline">Elevate Your Commercial Building's Efficiency<br>With Periodic HVAC Maintenance!</p>

  <div class="cta">Request Service</div>

  <section class="benefits">
    <div class="benefit benefit--orange"><div class="benefit-face">Reduce monthly power usage</div></div>
    <div class="benefit benefit--blue"><div class="benefit-face">Reduce emergency<br>HVAC service calls</div></div>
    <div class="benefit benefit--orange"><div class="benefit-face">Reduce costly<br>repairs costs</div></div>
    <div class="benefit benefit--blue"><div class="benefit-face">Reduce HVAC down-times<br>and angry tenants</div></div>
    <div class="benefit benefit--orange"><div class="benefit-face">Boosts HVAC lifespan of the existing and/or new HVAC equipment, Cut early replacement Costs!</div></div>
    <div class="benefit benefit--blue"><div class="benefit-face">Reduces tenant's early termination of their lease and law suits against the landlords</div></div>
    <div class="benefit benefit--orange"><div class="benefit-face">Increases tenant's renewal of the lease and agree to pay the increase rental rates</div></div>
    <div class="benefit benefit--blue"><div class="benefit-face">Reduces unhappy customers and increases tenant's productivity</div></div>
    <div class="benefit benefit--orange"><div class="benefit-face">Lower Expenses,<br>Increase Property Value,<br>Maximize ROI<br>(Return On Investment)</div></div>
  </section>

  <div class="photo photo--crew" role="img" aria-label="Overhead view of two technicians in hard hats servicing rooftop condenser fans"></div>
  <div class="photo photo--roof" role="img" aria-label="Commercial rooftop with exhaust stack, ducting and stairway"></div>

  <footer class="footer" role="img" aria-label="Blue-toned background of ventilation ductwork">
    <h2 class="partners"><b>Our Trusted</b> Partners</h2>
    <span class="divider"></span>
    <p class="promise">Trust a Reliable, Licensed HVAC<br>Partner for Periodic Maintenance.<br>Avoid Costly Repairs and<br>Ensure Longevity.</p>
  </footer>
</main>
</body>
</html>
```